Business Card Design Project

I need the following:

Logo -
Name - Dale Whitcomb
Title - Customer Experience Officer
Web - www.brvq.net
Phone - 555-418-3076
Updates

Project Deadline Extended
Reason: I launched the project later than anticipated. I look forward to seeing your designs. Dale

Industry/Entity Type

Business

```html
<!DOCTYPE html>
<html lang="en">
<head>
<meta charset="utf-8">
<title>Dale Whitcomb – Business Card</title>
<link href="https://fonts.googleapis.com/css2?family=Titillium+Web:wght@600;700;900&display=swap" rel="stylesheet">
<style>
  :root {
    --navy: #1f3566;
    --sky: #0a8ac4;
    --ink: #111111;
    --paper: #ffffff;
    --backdrop: #e6e6e6;
    --mark: #1d5fa8;
  }
  * { margin: 0; padding: 0; box-sizing: border-box; }
  html, body {
    width: 1200px; height: 772px; overflow: hidden;
    background: var(--backdrop);
    font-family: "Titillium Web", sans-serif;
  }
  .card {
    position: absolute; left: 50px; top: 72px;
    width: 1100px; height: 628px;
    background: var(--paper);
    overflow: hidden;
  }
  .edge { position: absolute; top: 0; width: 28px; height: 100%; }
  .edge--left { left: 0; }
  .edge--right { right: 0; width: 30px; }
  .edge span { display: block; height: 50%; }
  .edge--left .edge-top, .edge--right .edge-bottom { background: var(--navy); }
  .edge--left .edge-bottom, .edge--right .edge-top { background: var(--sky); }

  .brand {
    position: absolute; left: 340px; top: 82px;
    display: flex; align-items: center; gap: 32px;
  }
  .brand-dot {
    width: 140px; height: 140px; border-radius: 50%;
    background: var(--mark);
  }
  .brand-text { display: flex; flex-direction: column; }
  .brand-name {
    font-weight: 900; font-size: 35px; line-height: 30px;
    color: var(--ink); text-transform: uppercase; letter-spacing: 0.5px;
  }
  .brand-site {
    margin-top: 8px; padding-top: 2px;
    display: flex; align-items: center; gap: 8px;
    font-weight: 700; font-size: 15px; color: var(--sky);
  }
  .brand-site::before, .brand-site::after {
    content: ""; flex: 1; height: 2px; background: var(--sky);
  }

  .person { position: absolute; left: 0; width: 100%; top: 312px; text-align: center; color: var(--ink); }
  .person-name { font-weight: 700; font-size: 41px; line-height: 52px; text-transform: uppercase; }
  .person-title { font-weight: 600; font-size: 20px; line-height: 28px; }

  .contact {
    position: absolute; left: 0; width: 100%; top: 464px;
    list-style: none; text-align: center; color: var(--ink);
    font-weight: 700; font-size: 23px; line-height: 37px; text-transform: uppercase;
  }
</style>
</head>
<body>
  <div class="card">
    <div class="edge edge--left"><span class="edge-top"></span><span class="edge-bottom"></span></div>
    <div class="edge edge--right"><span class="edge-top"></span><span class="edge-bottom"></span></div>

    <div class="brand">
      <div class="brand-dot" aria-hidden="true"></div>
      <div class="brand-text">
        <span class="brand-name">Broadreach</span>
        <span class="brand-name">Voice</span>
        <span class="brand-name">Consulting</span>
        <span class="brand-site">www.brvq.net</span>
      </div>
    </div>

    <div class="person">
      <h1 class="person-name">Dale Whitcomb</h1>
      <p class="person-title">Customer Experience Officer</p>
    </div>

    <ul class="contact">
      <li class="contact-phone">555-418-3076</li>
      <li class="contact-web">www.brvq.net</li>
      <li class="contact-address">Harbor Line Services Inc 00 Ave Milton, NJ 00000</li>
    </ul>
  </div>
</body>
</html>
```